Trifold brochure for Thai yoga massage practice (In a Combat gym and a Spa)

I am a Practitioner of Thai massage in Toronto, and will in the near future be offering personal training with transitional fitness from couch potato to weekend warriors.

I train in Muay-thai and my current stream of clients are "thai tigers" in need of restorative therapy to get them back on their feet - hence the website name Fernquiet.com.
My other stream of clients are in a Lovely Spa on a rooftop patio (if you're ever in Toronto come on by).

So I have the best of two worlds (injuries vs. pure bliss) Dark vs. Light

I want to introduce Thai yoga massage to a new modern audience. Thai massage is an ancient, effective hybrid therapy incorporating traditional acupressure/ body meridian therapy and human kinetics simultaneously.

Brochures are meant for distribution to martial arts studios, fitness gyms and other spas.

I am open to eye-catching, out of the box ideas.

My website: www.fernquiet.com (I am in the process of editing this new web space - apologies for the very basic nature of it)

Pictures are attached for review or view my link:
https://files.plumdock.net/share?id=7QX41mKpLw93_rTbNvEhYcUaZdJ2&view=open

Thank you!

Target Market(s)

20-45 year old fitness enthusiast for a gym audience
or 20-55 year old looking for general wellness/ relaxation
or combination of both (yin/yang type design)

Industry/Entity Type

Training

Font styles to use
Decorative

Requirements
Must have
• Will be looking for innovation, clever, witty design, please be creative. Toronto is a quirky city, I welcome quirky, yet tasteful designs.

Please use a good amount of flow, and streaming lines.
Nice to have
• If we could have a yin / yang effect that would be nice (Combat restoration vs. Relaxation)
Should not have
• Please do not have text / designs that convey the stereotypical nonsense that surround Asian based massage (my cup is full already).

```html
<!DOCTYPE html>
<html lang="en">
<head>
<meta charset="utf-8">
<title>Fernquiet – Thai Yoga Massage Brochure</title>
<link rel="stylesheet" href="https://fonts.googleapis.com/css2?family=Montserrat:wght@700;800&family=Questrial&display=swap">
<style>
  :root {
    --stage: #e4e4e4;
    --ink-dark: #2a2b2f;
    --ink-dark-2: #34353a;
    --stone: #b8bbb7;
    --signal-red: #c1272b;
    --paper-text: #e8e8e8;
    --stone-text: #2e2f31;
    --fold: rgba(0,0,0,0.18);
  }
  * { box-sizing: border-box; margin: 0; padding: 0; }
  html, body { width: 1200px; height: 1000px; overflow: hidden; background: var(--stage); }
  body { position: relative; font-family: "Questrial", sans-serif; }

  .brochure {
    position: absolute; left: 45px; top: 130px;
    width: 1110px; height: 740px;
    background: var(--stone);
    overflow: hidden;
    box-shadow: 0 12px 30px rgba(0,0,0,0.18);
  }
  .brochure__shapes { position: absolute; inset: 0; }

  .photo { position: absolute; }
  .photo--session { left: 30px; top: 392px; width: 178px; height: 112px;
    border: 5px solid var(--signal-red);
    background: linear-gradient(135deg, #8d8f93 0%, #4b4a4e 45%, #cfcfcf 100%); }
  .photo--compress { left: 420px; top: 100px; width: 290px; height: 340px;
    background: radial-gradient(ellipse at 45% 35%, #e6e2d4 0%, #d8d2c0 28%, #8e2a26 55%, #6b1f1c 75%, #f1f1ef 100%); }
  .photo--stretch-red { left: 960px; top: 40px; width: 150px; height: 400px;
    background: linear-gradient(200deg, #3a3b3f 0%, #c9322e 35%, #b52723 60%, #d7a488 100%); }
  .photo--back { left: 740px; top: 440px; width: 370px; height: 300px;
    background: linear-gradient(160deg, #3b4aa8 0%, #2f3d9a 45%, #6b4a38 70%, #2a3580 100%); }

  .heading {
    position: absolute;
    font-family: "Montserrat", sans-serif; font-weight: 800;
    text-transform: uppercase; letter-spacing: 0.5px; line-height: 1;
  }
  .heading--light { color: #ffffff; }
  .heading--dark { color: var(--stone-text); }

  .copy { position: absolute; font-size: 11px; line-height: 1.42; text-align: justify; }
  .copy p + p { margin-top: 8px; }
  .copy--on-dark { color: var(--paper-text); }
  .copy--on-stone { color: var(--stone-text); }

  .intro-heading { left: 30px; top: 32px; font-size: 25px; }
  .intro-copy { left: 30px; top: 72px; width: 310px; }

  .heat-heading { left: 40px; top: 528px; font-size: 22px; }
  .heat-copy { left: 40px; top: 562px; width: 300px; }

  .tools-heading { left: 400px; top: 478px; font-size: 22px; }
  .tools-copy { left: 400px; top: 512px; width: 310px; }

  .contrast-copy { left: 770px; top: 150px; width: 175px; font-size: 11.5px; line-height: 1.5; }

  .tagline { position: absolute; left: 760px; top: 384px; }
  .tagline__title { font-family: "Montserrat", sans-serif; font-weight: 800; font-size: 21px; line-height: 1; color: #fff; text-transform: uppercase; }
  .tagline__url { font-family: "Montserrat", sans-serif; font-weight: 700; font-size: 8px; letter-spacing: 3px; color: #fff; text-transform: uppercase; margin-top: 5px; }
</style>
</head>
<body>
  <main class="brochure">
    <svg class="brochure__shapes" width="1110" height="740" viewBox="0 0 1110 740">
      <rect width="1110" height="740" fill="var(--stone)"/>
      <path d="M0 0 H370 V345 C300 356 240 372 0 392 Z" fill="var(--ink-dark)"/>
      <path d="M0 392 C240 372 300 356 370 345 V380 C300 394 240 412 0 434 Z" fill="var(--signal-red)"/>
      <path d="M370 0 H740 V300 C640 315 500 325 370 330 Z" fill="var(--ink-dark-2)"/>
      <path d="M370 330 C500 325 640 315 740 300 V335 C640 350 500 360 370 362 Z" fill="var(--signal-red)"/>
      <path d="M740 0 H1110 V350 C1000 360 860 370 740 375 Z" fill="var(--ink-dark)"/>
      <path d="M740 375 C860 370 1000 360 1110 350 V420 C1000 432 860 440 740 444 Z" fill="var(--signal-red)"/>
      <line x1="370" y1="0" x2="370" y2="740" stroke="var(--fold)" stroke-width="1.5"/>
      <line x1="740" y1="0" x2="740" y2="740" stroke="var(--fold)" stroke-width="1.5"/>
    </svg>

    <div class="photo photo--session" role="img" aria-label="Photo of a practitioner guiding a client through a Thai yoga stretch on a mat"></div>
    <div class="photo photo--compress" role="img" aria-label="Photo of two cloth herbal compress balls and wooden sticks on a white plate over a red patterned cloth"></div>
    <div class="photo photo--back" role="img" aria-label="Photo of a client in a blue shirt lying face down receiving back massage"></div>
    <div class="photo photo--stretch-red" role="img" aria-label="Photo of a practitioner in red pressing on a client's back"></div>

    <h2 class="heading heading--light intro-heading">Thai Yoga Massage</h2>
    <div class="copy copy--on-dark intro-copy">
      <p>This form of bodywork therapy is 2500 years in the making and is practiced and regulated in Thailand today. With many different lineages and styles the concept of Thai Yoga Massage is the same.</p>
      <p>A session is commenced traditionally on a padded floor or mat with the client clothed in comfortable garments that allow freedom of movement.</p>
      <p>Through the placement of the client's body in a series of yoga like poses a trained practitioner is able to establish levels of structural balance. A combination of rhythmic techniques with specific poses allows the practitioner to stimulate the Sen (synonymous with energy lines or meridians), isolate and release trigger points in a client.</p>
    </div>

    <h2 class="heading heading--dark heat-heading">Thai Heat Therapy</h2>
    <div class="copy copy--on-stone heat-copy">
      <p>This form of bodywork therapy is 2500 years in the making and is practiced and regulated in Thailand today. With many different lineages and styles the concept of Thai Yoga Massage is the same.</p>
    </div>

    <h2 class="heading heading--dark tools-heading">What I Use.</h2>
    <div class="copy copy--on-stone tools-copy">
      <p>This form of bodywork therapy is 2500 years in the making and is practiced and regulated in Thailand today. With many different lineages and styles the concept of Thai Yoga Massage is the same.</p>
    </div>

    <div class="copy copy--on-dark contrast-copy">
      <p>This form of bodywork therapy is 2500 years in the making and is practiced and regulated in Thailand today. With many different lineages and styles the concept of Thai Yoga Massage is the same.</p>
    </div>

    <div class="tagline">
      <div class="tagline__title">Dark vs. Light</div>
      <div class="tagline__url">www.fernquiet.com</div>
    </div>
  </main>
</body>
</html>
```